Quorvin Upcoming Gigs

One page graphic with my upcoming dates. Logo and photo attached, and sample from last flyer. Text:

QUORVIN

UPCOMING DATES

3/26/18 Tidal Plums (Las Vegas, NV)

4/1/18 Venture Hollow 2847 M St (Sac, CA)

4/8/18 Amber Heron (Sac, CA)

5/5/18 Low Ceiling @ Silver Moth (Sac, CA)

5/10/18 Pellman Art Museum (Sac, CA)

5/11/18 Vif Brume @ Cafe du Lierre (Sac, CA)

5/27/18 Sonnlicht JTR @ Vox (Sac, CA)

Save The Date: 9/21/18 Lanterns Festival (Puerto Nuevo, MX)

plazabook.example/quorvin482

Target Market(s)

House/Electronic Music

Industry/Entity Type

Night Club

Font styles to use
Sans Serif

Colors

Designer to choose colors to be used in the design.

Requirements
Must have
• Quorvin logo or something that looks good instead. Prefer photo to be in but not necessary.
Nice to have

```html
<!DOCTYPE html>
<html lang="en">
<head>
<meta charset="utf-8">
<title>Quorvin Upcoming Dates</title>
<link href="https://fonts.googleapis.com/css2?family=Oswald:wght@600;700&family=Open+Sans:wght@400;600&display=swap" rel="stylesheet">
<style>
  :root {
    --page-bg: #e6e6e8;
    --flyer-black: #0a0709;
    --brand-blue: #2a40b0;
    --box-blue: #2437a6;
    --white: #ffffff;
    --bronze: #5a4a30;
    --bronze-dark: #3a2e1e;
    --photo-magenta: #8a1f5a;
    --photo-purple: #3b1f6e;
    --photo-amber: #6b4a2a;
  }
  * { box-sizing: border-box; margin: 0; padding: 0; }
  html, body { width: 1200px; height: 1200px; overflow: hidden; }
  body {
    background: var(--page-bg);
    font-family: "Open Sans", sans-serif;
    position: relative;
  }
  .flyer {
    position: absolute;
    left: 175px; top: 50px;
    width: 850px; height: 1100px;
    background: var(--flyer-black);
    overflow: hidden;
  }
  .flyer__photo {
    position: absolute;
    left: 0; top: 0; width: 850px; height: 900px;
    background:
      radial-gradient(ellipse 300px 260px at 330px 360px, var(--photo-magenta), transparent 70%),
      radial-gradient(ellipse 360px 300px at 220px 280px, var(--photo-purple), transparent 75%),
      radial-gradient(ellipse 500px 260px at 420px 700px, var(--photo-amber), transparent 75%),
      var(--flyer-black);
  }
  .brand {
    position: absolute;
    top: 30px; left: 0; width: 100%;
    text-align: center;
    font-family: "Oswald", sans-serif;
    font-weight: 700;
    font-size: 130px;
    letter-spacing: 6px;
    color: var(--brand-blue);
    line-height: 1;
  }
  .headline {
    position: absolute;
    left: 70px; top: 520px;
    font-family: "Oswald", sans-serif;
    font-weight: 700;
    color: var(--white);
    line-height: 0.95;
    text-transform: uppercase;
  }
  .headline__name { display: block; font-size: 70px; padding-left: 150px; }
  .headline__title { display: block; font-size: 104px; }
  .dates {
    position: absolute;
    left: 28px; top: 770px; width: 794px;
    display: grid;
    grid-template-columns: repeat(4, 185px);
    column-gap: 18px; row-gap: 18px;
  }
  .date-card {
    background: var(--box-blue);
    border-radius: 12px;
    height: 82px;
    color: var(--white);
    text-align: center;
    display: flex; flex-direction: column; justify-content: center;
    line-height: 1.15;
  }
  .date-card--offset { transform: translateX(101px); }
  .date-card__day { font-size: 24px; font-weight: 400; }
  .date-card__venue { font-size: 12.5px; }
  .save-date {
    position: absolute;
    left: 0; width: 100%; top: 968px;
    text-align: center;
    color: var(--white);
    font-size: 22px;
    text-transform: uppercase;
  }
  .feature-band {
    position: absolute;
    left: 0; top: 1002px; width: 100%; height: 62px;
    background: linear-gradient(90deg, var(--bronze-dark), var(--bronze), var(--bronze-dark));
    color: var(--white);
    font-size: 32px;
    text-align: center;
    line-height: 62px;
  }
</style>
</head>
<body>
  <main class="flyer">
    <div class="flyer__photo" role="img" aria-label="Photo of the DJ performing at the decks under magenta and purple club lights"></div>
    <div class="brand">QUORVIN</div>
    <h1 class="headline">
      <span class="headline__name">Quorvin</span>
      <span class="headline__title">Upcoming Dates</span>
    </h1>
    <section class="dates">
      <div class="date-card"><span class="date-card__day">3/26/18</span><span class="date-card__venue">Tidal Plums<br>(Las Vegas, NV)</span></div>
      <div class="date-card"><span class="date-card__day">4/1/18</span><span class="date-card__venue">Venture Hollow 2847 M St<br>(Sac, CA)</span></div>
      <div class="date-card"><span class="date-card__day">4/8/18</span><span class="date-card__venue">Amber Heron<br>(Sac, CA)</span></div>
      <div class="date-card"><span class="date-card__day">5/5/18</span><span class="date-card__venue">Low Ceiling @ Silver Moth<br>(Sac, CA)</span></div>
      <div class="date-card date-card--offset"><span class="date-card__day">5/10/18</span><span class="date-card__venue">Pellman Art Museum<br>(Sac, CA)</span></div>
      <div class="date-card date-card--offset"><span class="date-card__day">5/11/18</span><span class="date-card__venue">Vif Brume @ Cafe du Lierre<br>(Sac, CA)</span></div>
      <div class="date-card date-card--offset"><span class="date-card__day">5/27/18</span><span class="date-card__venue">Sonnlicht JTR @ Vox<br>(Sac, CA)</span></div>
    </section>
    <p class="save-date">Save the Date</p>
    <p class="feature-band">9/21/18 Lanterns Festival (Puerto Nuevo, MX)</p>
  </main>
</body>
</html>
```